Need Icons design for timeline

We want to use a timeline component (http://chronoline.example-plume.net/) to show business synergy history. Our business is petrochemical and refinery.

We need the following images.
1. Icon: Business Development (BD) - size 30x30 px
2. Icon: Merger and Acquisition (MA) - size 30x30 px
3. Icon: Synergy - size 30x30 px
4. Image for Timeline progress as attached. Width = 700px
4.1 Show Year for each progress
4.2 Has indicator showing the active progress or highlight the active progress
4.3 There are 3 progresses
- Facing Financial Crisis
- Huge New Capacity & Economic Downturn
- Global Competition

Reason: Customer provides more detail as updated in the Must have features section.

Industry/Entity Type

Business

Requirements
Must have
• 1. All 3 icons must have white (transparent background) without border.
2. "Business Development" icon should use picture that represents business growth. For example, a rising chart.
3. "Merger and Acquisition" icon should use picture that represents two parties agreeing on something. For example, two people shaking hands.
4. "Synergy" icon should use picture that represents small parts forming a big picture. For example, jigsaw.
5. There should not be too much detail on the icons because they will be resized to 30x30 pixels.

```html
<!DOCTYPE html>
<html lang="en">
<head>
<meta charset="utf-8">
<title>Timeline Icons</title>
<link href="https://fonts.googleapis.com/css2?family=Source+Sans+3:wght@400;600;700&display=swap" rel="stylesheet">
<style>
  :root {
    --bg: #ffffff;
    --label: #2b2b2b;
    --year: #8a8a8a;
    --bd-blue-dark: #2a6fb8;
    --bd-teal-dark: #3a86a8;
    --ma-green: #74b42e;
    --ma-green-light: #a4d65e;
    --ma-green-dark: #4a8212;
    --ma-outline: #5b7fd6;
    --syn-orange: #eba34a;
    --syn-grey: #5e5e5e;
    --syn-grey-dark: #333333;
  }
  html, body { margin: 0; padding: 0; overflow: hidden; background: var(--bg); }
  .canvas { position: relative; width: 1200px; height: 604px; background: var(--bg); font-family: "Source Sans 3", sans-serif; }
  .icon-card { position: absolute; top: 42px; width: 180px; text-align: center; }
  .icon-card svg { display: block; margin: 0 auto; width: 86px; height: 86px; }
  .icon-label { margin-top: 20px; font-size: 20px; line-height: 21px; color: var(--label); }
  .timeline { position: absolute; left: 18px; width: 820px; height: 56px; }
  .timeline text { font-family: "Source Sans 3", sans-serif; }
  .year { position: absolute; font-size: 23px; font-weight: 700; color: var(--year); }
</style>
</head>
<body>
<div class="canvas">

  <svg width="0" height="0" style="position:absolute">
    <defs>
      <linearGradient id="g-blue" x1="0" y1="0" x2="0" y2="1"><stop offset="0" stop-color="#5db4f2"/><stop offset="1" stop-color="#2c7fd2"/></linearGradient>
      <linearGradient id="g-green" x1="0" y1="0" x2="0" y2="1"><stop offset="0" stop-color="#9ccf48"/><stop offset="1" stop-color="#5f9d1c"/></linearGradient>
      <linearGradient id="g-orange" x1="0" y1="0" x2="0" y2="1"><stop offset="0" stop-color="#f4bd5c"/><stop offset="1" stop-color="#de8f28"/></linearGradient>
      <linearGradient id="g-sky" x1="0" y1="0" x2="0" y2="1"><stop offset="0" stop-color="#7ccbe4"/><stop offset="1" stop-color="#3a8db6"/></linearGradient>
      <linearGradient id="g-royal" x1="0" y1="0" x2="0" y2="1"><stop offset="0" stop-color="#6c8fdc"/><stop offset="1" stop-color="#2c4ea4"/></linearGradient>
      <linearGradient id="g-grey" x1="0" y1="0" x2="0" y2="1"><stop offset="0" stop-color="#7a7a7a"/><stop offset="1" stop-color="#333333"/></linearGradient>
      <linearGradient id="g-puzzle-orange" x1="0" y1="0" x2="0" y2="1"><stop offset="0" stop-color="#f2b862"/><stop offset="1" stop-color="#df8d2c"/></linearGradient>
      <linearGradient id="g-puzzle-grey" x1="0" y1="0" x2="0" y2="1"><stop offset="0" stop-color="#777"/><stop offset="1" stop-color="#3c3c3c"/></linearGradient>

      <g id="easel-chart">
        <polyline points="16,44 30,30 40,37 58,20" fill="none" stroke="#fff" stroke-width="4" stroke-linejoin="round"/>
        <polygon points="50,15 65,13 63,28" fill="#fff"/>
      </g>

      <path id="heart" d="M40 75 C20 59 3 47 3 27 C3 13 14 5 25 5 C32 5 37 9 40 13 C43 9 48 5 55 5 C66 5 77 13 77 27 C77 47 60 59 40 75Z"/>
      <g id="hands">
        <path d="M8 34 L20 22 L28 30 L16 42Z"/>
        <path d="M72 34 L60 22 L52 30 L64 42Z"/>
        <path d="M22 26 L36 20 L48 22 L58 28 L60 36 L48 60 L40 60 L26 46 L20 38Z"/>
        <path d="M36 20 L30 30 Q34 34 40 30 L46 26" />
        <path d="M30 40 L42 30 M34 46 L47 34 M39 52 L51 40 M44 57 L55 45"/>
      </g>

      <g id="puzzle-cuts" fill="none" stroke="#fff" stroke-width="3">
        <path d="M40 4 V14 a7 7 0 1 0 0 14 V38"/>
        <path d="M40 38 V48 a7 7 0 1 1 0 14 V72"/>
        <path d="M6 38 H16 a7 7 0 1 1 14 0 H40"/>
        <path d="M40 38 H50 a7 7 0 1 0 14 0 H74"/>
      </g>
    </defs>
  </svg>

  <!-- Set one: colour icons -->
  <div class="icon-card" style="left:0px">
    <svg viewBox="0 0 80 80" aria-hidden="true">
      <rect x="36" y="0" width="8" height="6" fill="var(--bd-blue-dark)"/>
      <rect x="30" y="4" width="20" height="4" fill="var(--bd-blue-dark)"/>
      <rect x="6" y="8" width="68" height="46" rx="3" fill="url(#g-blue)"/>
      <use href="#easel-chart"/>
      <rect x="2" y="53" width="76" height="5" rx="1" fill="var(--bd-blue-dark)"/>
      <path d="M40 58 L24 79 M40 58 L56 79 M40 58 L40 72" stroke="var(--bd-blue-dark)" stroke-width="4"/>
    </svg>
    <div class="icon-label">Business<br>Development</div>
  </div>

  <div class="icon-card" style="left:177px">
    <svg viewBox="0 0 80 80" aria-hidden="true">
      <use href="#heart" fill="var(--ma-green)" stroke="var(--ma-green-dark)" stroke-width="3"/>
      <use href="#hands" fill="var(--ma-green-light)" stroke="var(--ma-green-dark)" stroke-width="2.5" stroke-linejoin="round" stroke-linecap="round"/>
    </svg>
    <div class="icon-label">Merger &amp;<br>Acquisition</div>
  </div>

  <div class="icon-card" style="left:342px">
    <svg viewBox="0 0 80 80" aria-hidden="true">
      <rect x="6" y="4" width="68" height="68" fill="url(#g-puzzle-orange)"/>
      <rect x="2" y="51" width="6" height="6" fill="#df8d2c"/>
      <circle cx="2" cy="54" r="6" fill="#df8d2c"/>
      <circle cx="74" cy="21" r="6" fill="#fff"/>
      <circle cx="57" cy="72" r="6" fill="#fff"/>
      <use href="#puzzle-cuts"/>
    </svg>
    <div class="icon-label">Synergy</div>
  </div>

  <!-- Set two: alternate palette icons -->
  <div class="icon-card" style="left:646px">
    <svg viewBox="0 0 80 80" aria-hidden="true">
      <rect x="36" y="0" width="8" height="6" fill="var(--bd-teal-dark)"/>
      <rect x="30" y="4" width="20" height="4" fill="var(--bd-teal-dark)"/>
      <rect x="6" y="8" width="68" height="46" rx="3" fill="url(#g-sky)"/>
      <use href="#easel-chart"/>
      <rect x="2" y="53" width="76" height="5" rx="1" fill="var(--bd-teal-dark)"/>
      <path d="M40 58 L24 79 M40 58 L56 79 M40 58 L40 72" stroke="var(--bd-teal-dark)" stroke-width="4"/>
    </svg>
    <div class="icon-label">Business<br>Development</div>
  </div>

  <div class="icon-card" style="left:823px">
    <svg viewBox="0 0 80 80" aria-hidden="true">
      <use href="#heart" fill="#fff" stroke="var(--ma-outline)" stroke-width="3"/>
      <use href="#hands" fill="#fff" stroke="var(--ma-outline)" stroke-width="2.5" stroke-linejoin="round" stroke-linecap="round"/>
    </svg>
    <div class="icon-label">Merger &amp;<br>Acquisition</div>
  </div>

  <div class="icon-card" style="left:988px">
    <svg viewBox="0 0 80 80" aria-hidden="true">
      <rect x="6" y="4" width="68" height="68" fill="url(#g-puzzle-grey)"/>
      <rect x="2" y="51" width="6" height="6" fill="var(--syn-grey-dark)"/>
      <circle cx="2" cy="54" r="6" fill="var(--syn-grey-dark)"/>
      <circle cx="74" cy="21" r="6" fill="#fff"/>
      <circle cx="57" cy="72" r="6" fill="#fff"/>
      <use href="#puzzle-cuts"/>
    </svg>
    <div class="icon-label">Synergy</div>
  </div>

  <!-- Timeline one -->
  <svg class="timeline" style="top:272px" viewBox="0 0 700 48" aria-label="Timeline progress">
    <polygon points="453,1 675,1 697,24 675,47 453,47 475,24" fill="url(#g-orange)"/>
    <polygon points="231,1 453,1 475,24 453,47 231,47 253,24" fill="url(#g-green)"/>
    <path d="M4 1 H231 L253 24 L231 47 H4 Q0 47 0 43 V5 Q0 1 4 1Z" fill="url(#g-blue)"/>
    <g fill="#1b3a5c"><rect x="22" y="14" width="3" height="20"/><rect x="22" y="31" width="20" height="3"/><rect x="27" y="18" width="3" height="13"/><rect x="32" y="22" width="3" height="9"/><rect x="37" y="25" width="3" height="6"/></g>
    <text x="54" y="29" font-size="16" fill="#1b3a5c">Facing Financial Crisis</text>
    <g fill="#1f330a"><rect x="258" y="14" width="3" height="20"/><rect x="258" y="31" width="20" height="3"/><rect x="263" y="24" width="3" height="7"/><rect x="268" y="20" width="3" height="11"/><rect x="273" y="16" width="3" height="15"/></g>
    <text x="293" y="20" font-size="16" fill="#1f330a">Huge New Capacity &amp;</text>
    <text x="293" y="37" font-size="16" fill="#1f330a">Economic Downturn</text>
    <g fill="none"><circle cx="497" cy="23" r="11" fill="#4a2a05"/><path d="M486 23 H508 M497 12 V34 M488 17 H506 M488 29 H506" stroke="#e7a33d" stroke-width="1.5"/><ellipse cx="497" cy="23" rx="5" ry="11" stroke="#e7a33d" stroke-width="1.5"/></g>
    <text x="523" y="29" font-size="16" fill="#5f3406">Global Competition</text>
  </svg>
  <div class="year" style="left:253px;top:331px">2009</div>
  <div class="year" style="left:515px;top:331px">2011</div>

  <!-- Timeline two -->
  <svg class="timeline" style="top:449px" viewBox="0 0 700 48" aria-label="Timeline progress, alternate palette">
    <polygon points="453,1 675,1 697,24 675,47 453,47 475,24" fill="url(#g-grey)"/>
    <polygon points="231,1 453,1 475,24 453,47 231,47 253,24" fill="url(#g-royal)"/>
    <path d="M4 1 H231 L253 24 L231 47 H4 Q0 47 0 43 V5 Q0 1 4 1Z" fill="url(#g-sky)"/>
    <g fill="#163a55"><rect x="22" y="14" width="3" height="20"/><rect x="22" y="31" width="20" height="3"/><rect x="27" y="18" width="3" height="13"/><rect x="32" y="22" width="3" height="9"/><rect x="37" y="25" width="3" height="6"/></g>
    <text x="54" y="29" font-size="16" fill="#163a55">Facing Financial Crisis</text>
    <g fill="#dfe8ff"><rect x="258" y="14" width="3" height="20"/><rect x="258" y="31" width="20" height="3"/><rect x="263" y="24" width="3" height="7"/><rect x="268" y="20" width="3" height="11"/><rect x="273" y="16" width="3" height="15"/></g>
    <text x="293" y="20" font-size="16" fill="#dfe8ff">Huge New Capacity &amp;</text>
    <text x="293" y="37" font-size="16" fill="#dfe8ff">Economic Downturn</text>
    <g fill="none"><circle cx="497" cy="23" r="11" fill="#ffffff"/><path d="M486 23 H508 M497 12 V34 M488 17 H506 M488 29 H506" stroke="#555" stroke-width="1.5"/><ellipse cx="497" cy="23" rx="5" ry="11" stroke="#555" stroke-width="1.5"/></g>
    <text x="523" y="29" font-size="16" fill="#dddddd">Global Competition</text>
  </svg>
  <div class="year" style="left:253px;top:508px">2009</div>
  <div class="year" style="left:515px;top:508px">2011</div>

</div>
</body>
</html>
```